BRISK Study flyer

I need help designing a flyer for a research study that will include brain imaging in adolescents. The info is in the attached document. The study is called the Brain Rhythms In School Kids (BRISK) study. Ideally this would be returned as a document that I can edit in the future as we will have several new recruitment phases (different age groups, etc. I also would love to have a logo designed as part of this project, but I recognize that might be a separate design request.

```html
<!DOCTYPE html>
<html lang="en">
<head>
<meta charset="utf-8">
<title>BRISK Study Flyer</title>
<link href="https://fonts.googleapis.com/css2?family=Bebas+Neue&family=Poppins:ital,wght@0,400;0,500;0,600;0,700;1,700&family=Lobster&display=swap" rel="stylesheet">
<style>
  :root{
    --ink:#2b1d66;
    --purple:#8a6bbb;
    --teal:#17847f;
    --white:#ffffff;
    --stage:#9a9aa0;
    --text:#2f2a45;
  }
  *{box-sizing:border-box;margin:0;padding:0}
  html,body{width:1200px;height:3656px;overflow:hidden}
  body{background:var(--stage);font-family:"Poppins",sans-serif;color:var(--text);position:relative}
  .flyer{position:absolute;left:80px;top:1092px;width:1040px;height:1472px;background:var(--white);overflow:hidden}
  .abs{position:absolute}
  .thought-art{left:40px;top:32px;width:124px;height:106px;border-radius:50%;background:radial-gradient(circle,#dfeeee 0%,#f4f9f9 70%,#fff 100%)}
  .portrait{left:64px;top:114px;width:412px;height:565px;background:linear-gradient(180deg,#e9e4e0 0%,#b89a86 35%,#2b8b86 62%,#1f7a75 100%);border-radius:6px 6px 0 0}
  .band{left:0;top:534px;width:1040px;height:145px;background:var(--purple)}
  .band p{position:absolute;left:504px;top:20px;width:478px;color:var(--white);font-size:19px;line-height:1.15;font-weight:500}
  .band em{font-weight:700}
  .brand{left:504px;top:54px;display:flex;align-items:center;gap:16px}
  .brand-dot{width:120px;height:120px;border-radius:50%;background:var(--teal)}
  .brand-name{font-family:"Bebas Neue",sans-serif;font-size:84px;line-height:.9;color:var(--ink)}
  .brand-sub{font-size:12px;font-weight:600;color:var(--purple);line-height:1.3;text-transform:uppercase;border-bottom:2px solid var(--teal);padding-bottom:6px;width:180px;margin-top:4px}
  .head1,.head2{font-family:"Bebas Neue",sans-serif;font-weight:400;font-size:70px;line-height:1;left:504px;white-space:nowrap}
  .head1{top:222px;color:var(--ink)}
  .head2{top:292px;color:var(--teal)}
  .sub{left:504px;top:372px;font-weight:600;font-size:32px;line-height:1.2;color:var(--ink);text-transform:uppercase}
  .section-title{left:43px;top:727px;font-weight:700;font-size:30px;line-height:1.15;color:var(--ink);text-transform:uppercase}
  .section-title span{display:inline-block;border-bottom:3px solid var(--ink)}
  .divider{left:476px;top:721px;height:507px;border-left:2px dashed #c9c0da}
  .steps{left:43px;top:830px;width:420px;list-style:none}
  .step{display:flex;gap:20px;margin-bottom:30px}
  .step-icon{flex:0 0 80px;height:80px;border-radius:50%;display:flex;align-items:center;justify-content:center}
  .step h3{font-size:19px;font-weight:700;text-transform:uppercase;line-height:1.2;margin-top:6px}
  .step p,.step li{font-size:16px;line-height:1.15;color:var(--ink)}
  .step ul{padding-left:16px;margin-top:3px}
  .step li{margin-bottom:8px;font-weight:500}
  .c-ink{color:var(--ink)} .c-teal{color:var(--teal)} .c-purple{color:var(--purple)}
  .bg-ink{background:var(--ink)} .bg-teal{background:var(--teal)} .bg-purple{background:var(--purple)}
  .scan-photo{left:512px;top:721px;width:479px;height:172px;border-radius:12px 12px 0 0;background:linear-gradient(110deg,#cfe6f7 0%,#6fb1e2 45%,#1d4f8a 100%)}
  .eligible{left:512px;top:893px;width:479px;height:168px;background:var(--teal);border-radius:0 0 12px 12px;padding:22px 30px;color:var(--white)}
  .eligible h3{font-size:20px;font-weight:600;text-transform:uppercase;margin-bottom:8px}
  .eligible li{list-style:none;display:flex;gap:12px;font-size:16.5px;line-height:1.1;margin-bottom:5px}
  .tick{flex:0 0 16px;height:16px;margin-top:2px}
  .comp-pill{left:570px;top:1133px;width:260px;height:72px;background:var(--ink);color:var(--white);font-size:20px;line-height:1.1;padding:14px 0 0 36px;clip-path:polygon(3% 0,100% 0,100% 100%,0 100%)}
  .comp-circle{left:803px;top:1081px;width:167px;height:167px;border-radius:50%;background:var(--purple);border:6px solid var(--ink);color:var(--white);font-family:"Bebas Neue",sans-serif;font-size:86px;display:flex;align-items:center;justify-content:center}
  .contact{left:43px;top:1256px;width:954px;height:73px;background:var(--ink);border-radius:6px 6px 0 0;display:flex;align-items:center;padding:0 22px;gap:40px}
  .contact-script{font-family:"Lobster",cursive;color:var(--white);font-size:36px;white-space:nowrap}
  .contact-ask{color:var(--white);font-size:16px;line-height:1.1;text-transform:uppercase;white-space:nowrap}
  .contact-mail{background:var(--white);color:var(--ink);font-size:17px;font-weight:500;padding:5px 14px;display:flex;align-items:center;gap:10px;border-radius:2px;white-space:nowrap}
  .footer{left:0;top:1329px;width:1040px;height:143px;background:var(--purple);display:flex;align-items:center;padding-left:62px}
  .org{display:flex;align-items:center;gap:16px;color:var(--white);font-size:30px;font-weight:500;width:390px;white-space:nowrap}
  .org-mark{width:60px;height:60px;background:var(--white);border-radius:4px}
  .footer-rule{width:0;height:72px;border-left:2px solid rgba(255,255,255,.6);margin:0 80px 0 0}
  .url{color:var(--white);font-weight:700;font-size:34px;white-space:nowrap}
</style>
</head>
<body>
<main class="flyer">
  <div class="abs thought-art" role="img" aria-label="Thought bubble with tangled scribble illustration"></div>
  <div class="abs band"><p>Northfield University researchers are seeking <em>girls age 10-17</em> for a study about brain activity in emotions and decision-making and how they relate to puberty, anxiety and depression.</p></div>
  <div class="abs portrait" role="img" aria-label="Photo of a thoughtful teenage girl in a teal hoodie resting her chin on her hand"></div>

  <div class="abs brand">
    <div class="brand-dot"></div>
    <div>
      <div class="brand-name">BRISK</div>
      <div class="brand-sub">Brain Rhythms In<br>School Kids</div>
    </div>
  </div>
  <h1 class="abs head1">ARE YOU THE PARENT OF</h1>
  <h2 class="abs head2">A CHILD AGE 10-17?</h2>
  <p class="abs sub">Do they worry or<br>overthink negative<br>emotions?</p>

  <h2 class="abs section-title"><span>Study participation</span><br><span>involves</span></h2>
  <div class="abs divider"></div>
  <ul class="abs steps">
    <li class="step">
      <div class="step-icon bg-ink"><svg width="40" height="40" viewBox="0 0 30 30" fill="none" stroke="#fff" stroke-width="2"><circle cx="10" cy="11" r="4"/><circle cx="21" cy="11" r="4"/><path d="M3 26c0-5 3-8 7-8s7 3 7 8M14 26c0-5 3-8 7-8s6 3 6 8"/></svg></div>
      <div><h3 class="c-ink">One one-hour interview</h3><p>(online or in-person) where your child will discuss their thoughts</p></div>
    </li>
    <li class="step">
      <div class="step-icon bg-teal"><svg width="40" height="40" viewBox="0 0 30 30" fill="none" stroke="#fff" stroke-width="2"><rect x="4" y="4" width="22" height="18" rx="2"/><path d="M8 10l2 2 3-3M15 11h7M8 16l2 2 3-3M15 17h7M11 26h8"/></svg></div>
      <div><h3 class="c-teal">Online questionnaires</h3><p>(parent and child)</p></div>
    </li>
    <li class="step">
      <div class="step-icon bg-purple"><svg width="40" height="40" viewBox="0 0 30 30" fill="none" stroke="#fff" stroke-width="2"><path d="M5 24V12a10 10 0 0 1 20 0v12"/><path d="M3 24h24M10 20h12"/><circle cx="15" cy="12" r="4"/></svg></div>
      <div><h3 class="c-purple">One two hour visit</h3>
        <ul><li>where your child will complete an MRI scan</li><li>answer questions about their puberty stage</li><li>have a small hair sample taken to study puberty hormones</li></ul></div>
    </li>
  </ul>

  <div class="abs scan-photo" role="img" aria-label="Photo of an MRI scanner room with brain scan images on monitors"></div>
  <div class="abs eligible">
    <h3>Your child may be eligible if they :</h3>
    <ul>
      <li><svg class="tick" viewBox="0 0 16 16"><circle cx="8" cy="8" r="8" fill="#fff"/><path d="M4.5 8.2l2.3 2.3 4.7-4.7" stroke="#17847f" stroke-width="2" fill="none"/></svg>Are age 10-17</li>
      <li><svg class="tick" viewBox="0 0 16 16"><circle cx="8" cy="8" r="8" fill="#fff"/><path d="M4.5 8.2l2.3 2.3 4.7-4.7" stroke="#17847f" stroke-width="2" fill="none"/></svg>Tend to worry or overthink negative thoughts</li>
      <li><svg class="tick" viewBox="0 0 16 16"><circle cx="8" cy="8" r="8" fill="#fff"/><path d="M4.5 8.2l2.3 2.3 4.7-4.7" stroke="#17847f" stroke-width="2" fill="none"/></svg>Have not been diagnosed with psychosis, learning problems, or autism</li>
    </ul>
  </div>
  <div class="abs comp-pill">Compensation<br>up to</div>
  <div class="abs comp-circle">$140</div>

  <div class="abs contact">
    <span class="contact-script">Please contact us</span>
    <span class="contact-ask">Interested in participating?<br>Want more information?</span>
    <span class="contact-mail"><svg width="22" height="16" viewBox="0 0 22 16" fill="none" stroke="#2b1d66" stroke-width="1.8"><rect x="1" y="1" width="20" height="14" rx="1"/><path d="M1 2l10 7 10-7"/></svg>briskstudy@northfieldhealth.org</span>
  </div>
  <footer class="abs footer">
    <div class="org"><span class="org-mark"></span>Northfield University</div>
    <div class="footer-rule"></div>
    <div class="url">www.northfield.edu</div>
  </footer>
</main>
</body>
</html>
```